Fun kids centric character and brand for premium cookies brand

Looking to start a cookies brand that provides fun story for kids. Creating a ‘boy’ version of jelly rascal with fun and cute character as per below inspiration.
Similar to the concept that Pipa lamb actually a girl, we wanted to create the Boy version of playful active cute and fun jelly rascal boy.
Color to be used shades of orange, brown and yellow

Target Market(s)

Kids, premium artisanal not supermarket

Font styles to use
Sans Serif

Colors
f37122
f68e4e
faa54b

Requirements
Must have
• Jellies rascal design and brand design “ Otto Pimble Rascal”. Big eyes, big nose, big teeth but not vampire kind
Nice to have
• Ideas on how to incorporates the character into japanese style comic strip for packaging and web as the next steps of application of the design
Should not have
• Scary, alien’ish character

```html
<!DOCTYPE html>
<html lang="en">
<head>
<meta charset="utf-8">
<title>Super Tasty Cookies – Pack Design</title>
<link href="https://fonts.googleapis.com/css2?family=Alfa+Slab+One&family=Kaushan+Script&family=Roboto+Slab:wght@400;700&family=Oswald:wght@300;400&family=Kalam:wght@700&family=Bree+Serif&display=swap" rel="stylesheet">
<style>
  :root {
    --bg: #f3f3f1;
    --white: #ffffff;
    --band-lime: #d6cf14;
    --orange-deep: #f37122;
    --orange-mid: #f68e4e;
    --orange-soft: #faa54b;
    --sun-core: #f9c51f;
    --sun-edge: #e8870f;
    --brown: #4a1b0b;
    --brown-soft: #6b2f16;
    --ink: #2a1a12;
    --tick: #f37122;
  }
  html, body {
    margin: 0;
    width: 1200px;
    height: 856px;
    overflow: hidden;
    background: var(--bg);
  }
  .canvas {
    position: relative;
    width: 1200px;
    height: 856px;
  }
  .pack {
    position: absolute;
    left: 250px;
    top: 38px;
    width: 700px;
    height: 780px;
  }
  .script { font-family: "Kaushan Script", cursive; }
  .headline { font-family: "Alfa Slab One", serif; }
  .slab { font-family: "Roboto Slab", serif; }
  .label-serif { font-family: "Bree Serif", serif; }
  .hand { font-family: "Kalam", cursive; font-weight: 700; }
  .condensed { font-family: "Oswald", sans-serif; font-weight: 300; }
</style>
</head>
<body>
<main class="canvas">
  <svg class="pack" viewBox="0 0 700 780" xmlns="http://www.w3.org/2000/svg">
    <defs>
      <radialGradient id="sunburst" cx="0.62" cy="0.55" r="0.75">
        <stop offset="0" stop-color="var(--sun-core)"/>
        <stop offset="0.6" stop-color="var(--orange-soft)"/>
        <stop offset="1" stop-color="var(--sun-edge)"/>
      </radialGradient>
      <radialGradient id="mascotTone" cx="0.5" cy="0.55" r="0.6">
        <stop offset="0" stop-color="#f7b52a"/>
        <stop offset="0.7" stop-color="#f0951c"/>
        <stop offset="1" stop-color="#f0951c" stop-opacity="0"/>
      </radialGradient>
      <path id="cookiesArc" d="M95 545 C160 400 310 300 505 330"/>
      <clipPath id="frontClip"><rect x="0" y="0" width="520" height="780"/></clipPath>
    </defs>

    <!-- front panel -->
    <g class="pack-front" clip-path="url(#frontClip)">
      <rect class="panel-base" x="0" y="0" width="520" height="780" fill="var(--white)"/>
      <rect class="seal-band" x="0" y="0" width="520" height="62" fill="#f7f7f7"/>
      <rect class="lime-band" x="0" y="62" width="520" height="22" fill="var(--band-lime)"/>
      <path class="sunburst-field" d="M0 84 H520 V330 C450 350 400 330 340 390 C270 460 160 500 0 570 Z" fill="url(#sunburst)"/>
      <path class="white-swoop" d="M0 570 C160 500 270 460 340 390 C400 330 450 350 520 330 V360 C450 380 410 360 350 420 C280 490 170 530 0 600 Z" fill="var(--white)" opacity="0.85"/>

      <text class="web-address label-serif" x="318" y="116" font-size="19" fill="var(--ink)" transform="rotate(4 318 116)">www.ottocrumbs.com</text>

      <text class="tagline script" x="70" y="255" font-size="40" fill="var(--brown)" transform="rotate(-28 70 255)">Super Tasty</text>

      <text class="headline-shadow headline" font-size="104" fill="var(--orange-deep)" transform="translate(5 6)">
        <textPath href="#cookiesArc" textLength="440" lengthAdjust="spacing">Cookies</textPath>
      </text>
      <text class="headline-main headline" font-size="104" fill="var(--brown)">
        <textPath href="#cookiesArc" textLength="440" lengthAdjust="spacing">Cookies</textPath>
      </text>

      <g class="mascot" role="img" aria-label="Illustration: fluffy orange rascal mascot hugging a cookie, with a thought bubble reading YES! and a small lightbulb">
        <ellipse cx="385" cy="600" rx="150" ry="185" fill="url(#mascotTone)"/>
        <ellipse cx="425" cy="420" rx="80" ry="55" fill="#f4ecdc"/>
      </g>

      <g class="product-name slab" fill="var(--brown)">
        <text x="22" y="640" font-size="84" font-weight="700">L</text>
        <text x="66" y="598" font-size="38">actation</text>
        <text x="66" y="634" font-size="38">cookies</text>
      </g>

      <g class="flavour-ribbon" transform="rotate(8 30 660)">
        <path d="M18 648 H210 L196 664 L210 680 H18 Z" fill="var(--brown)"/>
        <text class="script" x="28" y="670" font-size="16" fill="var(--white)">Cranberry &amp; Almond</text>
      </g>

      <g class="benefits hand" font-size="19" fill="var(--ink)">
        <g transform="rotate(6 30 706)">
          <path d="M24 700 l5 6 l9 -12" stroke="var(--tick)" stroke-width="3" fill="none"/>
          <text x="44" y="708">Tasty</text>
        </g>
        <g transform="rotate(6 30 732)">
          <path d="M22 726 l5 6 l9 -12" stroke="var(--tick)" stroke-width="3" fill="none"/>
          <text x="42" y="734">Healthy</text>
        </g>
        <g transform="rotate(6 30 758)">
          <path d="M20 752 l5 6 l9 -12" stroke="var(--tick)" stroke-width="3" fill="none"/>
          <text x="40" y="760">Crunchy</text>
        </g>
      </g>

      <g class="net-weight">
        <path d="M138 780 C146 742 178 716 228 708 V780 Z" fill="var(--orange-deep)"/>
        <text class="label-serif" x="176" y="750" font-size="30" fill="var(--white)">9<tspan font-size="16">oz</tspan></text>
        <text class="label-serif" x="166" y="772" font-size="14" fill="var(--white)">Net wt.</text>
      </g>
    </g>

    <!-- side panel -->
    <g class="pack-side">
      <rect x="520" y="0" width="180" height="780" fill="#fafafa"/>
      <rect x="520" y="0" width="180" height="62" fill="#f1f1f1"/>
      <rect x="520" y="62" width="180" height="22" fill="var(--band-lime)"/>
      <path d="M520 84 H700 V240 C640 250 570 280 520 300 Z" fill="var(--orange-soft)"/>
      <g class="facts condensed" font-size="13" fill="var(--ink)" text-anchor="end">
        <text x="680" y="280">Net weight 1kg</text>
        <text x="680" y="308">Batch No. 2008</text>
        <text x="680" y="336">MRP 10$</text>
        <text x="680" y="364">MFD date: 02-01-2018</text>
        <text x="680" y="392">Expiry date: 02-01-2019</text>
      </g>
      <text class="condensed" x="540" y="452" font-size="17" font-weight="400" fill="var(--ink)">ALL TYPES OF DESIGN</text>
      <g class="ingredients condensed" font-size="12" fill="var(--ink)">
        <text x="540" y="488">Ingredients: flour, butter, oats,</text>
        <text x="540" y="504">cranberry, almond, brown sugar,</text>
        <text x="540" y="520">honey.</text>
      </g>
      <g class="care-note condensed" font-size="10" fill="var(--ink)">
        <text x="540" y="566">Baked fresh in small batches with</text>
        <text x="540" y="580">care. No preservatives added.</text>
        <text x="540" y="594">Store in a cool dry place and</text>
        <text x="540" y="608">enjoy with milk.</text>
      </g>
    </g>
    <line x1="520" y1="0" x2="520" y2="780" stroke="#e2e2e2" stroke-width="1"/>
  </svg>
</main>
</body>
</html>
```